One Thumbnail for Online Shop for PowerPoint Templates needed

We are selling PowerPoint Templates and need therefore a thumbnail for our online shop.

You can use a stock photo, mock-ups or other design elements.

Format:
squared like 500 x 500
or wide like 1280 x 720

If you want to use a title, use:

"Graphs" ---> Title
"PowerPoint template" ---> subtitle

Attachments:
- OLD: Our old thumbnail which I do not like
- Template: PowerPoint pictures which you can use ( you can also copy them if you need more than these)
- Example: Some examples I found from other shops (please do not copy them exactly, only to show what I mean)

I received lots of designs until now but many are not what I have expected

Target Market(s)

E-Commerce

Industry/Entity Type

Shop

Font styles to use
Sans Serif

Requirements
Should not have
• Do NOT re-design one of the template.png (these are only examples, I will replace them later)

```html
<!DOCTYPE html>
<html lang="en">
<head>
<meta charset="utf-8">
<title>Standard Graphs – SlideCraft Presentation</title>
<link rel="stylesheet" href="https://fonts.googleapis.com/css2?family=Arvo&family=Lato:wght@300&family=Arimo:wght@400;700&display=swap">
<style>
  :root {
    --bg-light: #b8b2aa;
    --bg-mid: #6d655c;
    --bg-dark: #2b2a2b;
    --slide-bg: #f6f7f9;
    --slide-text: #222;
    --slide-muted: #8a8a8a;
    --bar-dark: #1f3f6e;
    --bar-light: #4e8fd6;
    --line-grey: #a9a9a9;
    --title-white: #ffffff;
  }
  html, body { margin: 0; padding: 0; overflow: hidden; }
  body { width: 1200px; height: 754px; background: var(--bg-dark); }
  .thumbnail {
    position: relative; width: 1200px; height: 754px; overflow: hidden;
    font-family: "Arimo", Arial, sans-serif;
  }
  .scene-photo {
    position: absolute; inset: 0;
    background:
      radial-gradient(ellipse 360px 260px at 650px 230px, rgba(230,232,236,.55), rgba(230,232,236,0) 70%),
      radial-gradient(ellipse 500px 300px at 1050px 220px, rgba(60,66,52,.6), rgba(60,66,52,0) 70%),
      linear-gradient(180deg, rgba(0,0,0,0) 50%, rgba(20,20,24,.75) 100%),
      linear-gradient(90deg, var(--bg-light) 0%, #9d958b 35%, var(--bg-mid) 65%, #3e3a35 100%);
  }
  .slide {
    position: absolute; left: 74px; width: 312px; height: 176px;
    background: var(--slide-bg);
    box-shadow: 0 1px 3px rgba(0,0,0,.25);
  }
  .slide svg { display: block; width: 100%; height: 100%; }
  .slide--columns { top: 80px; }
  .slide--growth { top: 296px; }
  .slide--ranking { top: 510px; }
  .slide-title { font: 700 13px "Arimo", Arial, sans-serif; fill: var(--slide-text); }
  .slide-lead { font: 400 7.3px "Arimo", Arial, sans-serif; fill: #444; }
  .chart-label { font: 700 5px "Arimo", Arial, sans-serif; fill: #333; }
  .micro { font: 400 3.8px "Arimo", Arial, sans-serif; fill: var(--slide-muted); }
  .axis-label { font: 400 5px "Arimo", Arial, sans-serif; fill: var(--slide-muted); }
  .value-in { font: 400 5.5px "Arimo", Arial, sans-serif; fill: #fff; text-anchor: middle; }
  .value-above { font: 400 5.5px "Arimo", Arial, sans-serif; fill: #777; text-anchor: middle; }
  .value-end { font: 400 4.6px "Arimo", Arial, sans-serif; fill: #333; }
  .pct { font: 400 4.4px "Arimo", Arial, sans-serif; fill: var(--bar-light); }
  .legend-light { font: 400 5.5px "Arimo", Arial, sans-serif; fill: var(--bar-light); }
  .legend-grey { font: 400 5.5px "Arimo", Arial, sans-serif; fill: #999; }
  .bar-dark { fill: var(--bar-dark); }
  .bar-light { fill: var(--bar-light); }
  .title-block { position: absolute; left: 448px; top: 464px; color: var(--title-white); }
  .title-main {
    margin: 0; font-family: "Arvo", Georgia, serif; font-weight: 400;
    font-size: 95px; line-height: 78px; letter-spacing: -1px;
  }
  .title-sub {
    margin: 18px 0 0 6px; font-family: "Lato", Arial, sans-serif; font-weight: 300;
    font-size: 47px; line-height: 1; letter-spacing: 2px; white-space: nowrap;
  }
</style>
</head>
<body>
<div class="thumbnail">
  <div class="scene-photo" role="img" aria-label="Photo of a desktop computer showing chart slides on a desk in a dimly lit room"></div>

  <svg width="0" height="0" style="position:absolute" aria-hidden="true">
    <defs>
      <symbol id="bullet-block" viewBox="0 0 90 36" overflow="visible">
        <circle cx="-4" cy="-1.2" r="0.8" fill="#999"/>
        <text class="micro" x="0" y="0">Lorem ipsum dolor sit amet,</text>
        <text class="micro" x="0" y="5.4">consectetur adipiscing elit, sed</text>
        <text class="micro" x="0" y="10.8">diam nonumy eirmod tempor</text>
        <text class="micro" x="0" y="16.2">invidunt ut labore et dolore</text>
        <text class="micro" x="0" y="21.6">magna aliquyam erat, sed diam</text>
        <text class="micro" x="0" y="27">voluptua. At vero eos.</text>
      </symbol>
    </defs>
  </svg>

  <!-- Slide: four column charts -->
  <div class="slide slide--columns">
    <svg viewBox="0 0 385 217">
      <text class="slide-title" x="192" y="20" text-anchor="middle">Lorem ipsum dolor sit amet</text>
      <text class="slide-lead" x="192" y="34" text-anchor="middle">Lorem ipsum dolor sit amet, consectetuer adipiscing elit. Aenean commodo ligula eget dolor.</text>

      <text class="chart-label" x="26" y="55">Lorem ipsum</text>
      <text class="micro" x="26" y="60">Lorem ipsum dolor sit amet, consectetur</text>
      <text class="chart-label" x="150" y="55">Lorem ipsum</text>
      <text class="micro" x="150" y="60">Lorem ipsum dolor sit amet, consectetur</text>
      <text class="chart-label" x="26" y="135">Lorem ipsum</text>
      <text class="micro" x="26" y="140">Lorem ipsum dolor sit amet, consectetur</text>
      <text class="chart-label" x="150" y="135">Lorem ipsum</text>
      <text class="micro" x="150" y="140">Lorem ipsum dolor sit amet, consectetur</text>

      <g transform="translate(30,115)">
        <line x1="-2" y1="0" x2="100" y2="0" stroke="#ccc" stroke-width=".5"/>
        <rect class="bar-light" x="0" y="-10" width="6" height="10"/><rect class="bar-dark" x="0" y="-6" width="6" height="6"/>
        <rect class="bar-light" x="10" y="-14" width="6" height="14"/><rect class="bar-dark" x="10" y="-9" width="6" height="9"/>
        <rect class="bar-light" x="20" y="-22" width="6" height="22"/><rect class="bar-dark" x="20" y="-14" width="6" height="14"/>
        <rect class="bar-light" x="30" y="-30" width="6" height="30"/><rect class="bar-dark" x="30" y="-18" width="6" height="18"/>
        <rect class="bar-light" x="40" y="-25" width="6" height="25"/><rect class="bar-dark" x="40" y="-16" width="6" height="16"/>
        <rect class="bar-light" x="50" y="-27" width="6" height="27"/><rect class="bar-dark" x="50" y="-18" width="6" height="18"/>
        <rect class="bar-light" x="60" y="-26" width="6" height="26"/><rect class="bar-dark" x="60" y="-17" width="6" height="17"/>
        <rect class="bar-light" x="70" y="-24" width="6" height="24"/><rect class="bar-dark" x="70" y="-15" width="6" height="15"/>
        <rect class="bar-light" x="80" y="-22" width="6" height="22"/><rect class="bar-dark" x="80" y="-14" width="6" height="14"/>
        <rect class="bar-light" x="90" y="-26" width="6" height="26"/><rect class="bar-dark" x="90" y="-17" width="6" height="17"/>
      </g>
      <g transform="translate(153,115)">
        <line x1="-2" y1="0" x2="100" y2="0" stroke="#ccc" stroke-width=".5"/>
        <rect class="bar-light" x="0" y="-12" width="6" height="12"/><rect class="bar-dark" x="0" y="-8" width="6" height="8"/>
        <rect class="bar-light" x="10" y="-28" width="6" height="28"/><rect class="bar-dark" x="10" y="-16" width="6" height="16"/>
        <rect class="bar-light" x="20" y="-22" width="6" height="22"/><rect class="bar-dark" x="20" y="-14" width="6" height="14"/>
        <rect class="bar-light" x="30" y="-40" width="6" height="40"/><rect class="bar-dark" x="30" y="-20" width="6" height="20"/>
        <rect class="bar-light" x="40" y="-34" width="6" height="34"/><rect class="bar-dark" x="40" y="-18" width="6" height="18"/>
        <rect class="bar-light" x="50" y="-30" width="6" height="30"/><rect class="bar-dark" x="50" y="-18" width="6" height="18"/>
        <rect class="bar-light" x="60" y="-25" width="6" height="25"/><rect class="bar-dark" x="60" y="-16" width="6" height="16"/>
        <rect class="bar-light" x="70" y="-28" width="6" height="28"/><rect class="bar-dark" x="70" y="-17" width="6" height="17"/>
        <rect class="bar-light" x="80" y="-24" width="6" height="24"/><rect class="bar-dark" x="80" y="-15" width="6" height="15"/>
        <rect class="bar-light" x="90" y="-30" width="6" height="30"/><rect class="bar-dark" x="90" y="-18" width="6" height="18"/>
      </g>
      <g transform="translate(30,195)">
        <line x1="-2" y1="0" x2="100" y2="0" stroke="#ccc" stroke-width=".5"/>
        <rect class="bar-light" x="0" y="-18" width="6" height="18"/><rect class="bar-dark" x="0" y="-12" width="6" height="12"/>
        <rect class="bar-light" x="10" y="-26" width="6" height="26"/><rect class="bar-dark" x="10" y="-16" width="6" height="16"/>
        <rect class="bar-light" x="20" y="-22" width="6" height="22"/><rect class="bar-dark" x="20" y="-14" width="6" height="14"/>
        <rect class="bar-light" x="30" y="-20" width="6" height="20"/><rect class="bar-dark" x="30" y="-13" width="6" height="13"/>
        <rect class="bar-light" x="40" y="-16" width="6" height="16"/><rect class="bar-dark" x="40" y="-11" width="6" height="11"/>
        <rect class="bar-light" x="50" y="-22" width="6" height="22"/><rect class="bar-dark" x="50" y="-14" width="6" height="14"/>
        <rect class="bar-light" x="60" y="-20" width="6" height="20"/><rect class="bar-dark" x="60" y="-13" width="6" height="13"/>
        <rect class="bar-light" x="70" y="-18" width="6" height="18"/><rect class="bar-dark" x="70" y="-12" width="6" height="12"/>
        <rect class="bar-light" x="80" y="-16" width="6" height="16"/><rect class="bar-dark" x="80" y="-11" width="6" height="11"/>
        <rect class="bar-light" x="90" y="-22" width="6" height="22"/><rect class="bar-dark" x="90" y="-14" width="6" height="14"/>
      </g>
      <g transform="translate(153,195)">
        <line x1="-2" y1="0" x2="100" y2="0" stroke="#ccc" stroke-width=".5"/>
        <rect class="bar-light" x="0" y="-22" width="6" height="22"/><rect class="bar-dark" x="0" y="-14" width="6" height="14"/>
        <rect class="bar-light" x="10" y="-30" width="6" height="30"/><rect class="bar-dark" x="10" y="-18" width="6" height="18"/>
        <rect class="bar-light" x="20" y="-36" width="6" height="36"/><rect class="bar-dark" x="20" y="-20" width="6" height="20"/>
        <rect class="bar-light" x="30" y="-40" width="6" height="40"/><rect class="bar-dark" x="30" y="-22" width="6" height="22"/>
        <rect class="bar-light" x="40" y="-38" width="6" height="38"/><rect class="bar-dark" x="40" y="-22" width="6" height="22"/>
        <rect class="bar-light" x="50" y="-36" width="6" height="36"/><rect class="bar-dark" x="50" y="-21" width="6" height="21"/>
        <rect class="bar-light" x="60" y="-34" width="6" height="34"/><rect class="bar-dark" x="60" y="-20" width="6" height="20"/>
        <rect class="bar-light" x="70" y="-30" width="6" height="30"/><rect class="bar-dark" x="70" y="-18" width="6" height="18"/>
        <rect class="bar-light" x="80" y="-28" width="6" height="28"/><rect class="bar-dark" x="80" y="-17" width="6" height="17"/>
        <rect class="bar-light" x="90" y="-32" width="6" height="32"/><rect class="bar-dark" x="90" y="-19" width="6" height="19"/>
      </g>
      <rect class="bar-light" x="262" y="180" width="3" height="3"/><text class="micro" x="267" y="183">Text</text>
      <rect class="bar-dark" x="262" y="187" width="3" height="3"/><text class="micro" x="267" y="190">Text</text>

      <use href="#bullet-block" x="292" y="75" width="90" height="36"/>
      <use href="#bullet-block" x="292" y="119" width="90" height="36"/>
      <use href="#bullet-block" x="292" y="163" width="90" height="36"/>
    </svg>
  </div>

  <!-- Slide: growth columns with line -->
  <div class="slide slide--growth">
    <svg viewBox="0 0 385 217">
      <text class="slide-title" x="192" y="20" text-anchor="middle">Lorem ipsum dolor sit amet</text>
      <text class="slide-lead" x="192" y="34" text-anchor="middle">Lorem ipsum dolor sit amet, consectetuer adipiscing elit. Aenean commodo ligula eget dolor.</text>

      <use href="#bullet-block" x="30" y="89" width="90" height="36"/>
      <use href="#bullet-block" x="30" y="146" width="90" height="36"/>

      <g class="growth-bars">
        <rect class="bar-light" x="116" y="149.6" width="11" height="39.4"/>
        <rect class="bar-light" x="133.5" y="146.6" width="11" height="42.4"/>
        <rect class="bar-light" x="151" y="137.5" width="11" height="51.5"/>
        <rect class="bar-light" x="168.5" y="125.4" width="11" height="63.6"/>
        <rect class="bar-light" x="186" y="122.3" width="11" height="66.7"/>
        <rect class="bar-light" x="203.5" y="116.3" width="11" height="72.7"/>
        <rect class="bar-light" x="221" y="110.2" width="11" height="78.8"/>
        <rect class="bar-light" x="238.5" y="101.1" width="11" height="87.9"/>
        <rect class="bar-light" x="256" y="101.1" width="11" height="87.9"/>
        <rect class="bar-light" x="273.5" y="95.1" width="11" height="93.9"/>
        <rect class="bar-light" x="291" y="92" width="11" height="97"/>
        <rect class="bar-light" x="308.5" y="86" width="11" height="103"/>
      </g>
      <g>
        <text class="value-in" x="121.5" y="171.3">13</text>
        <text class="value-in" x="139" y="169.8">14</text>
        <text class="value-in" x="156.5" y="165.3">17</text>
        <text class="value-in" x="174" y="159.2">21</text>
        <text class="value-in" x="191.5" y="157.7">22</text>
        <text class="value-in" x="209" y="154.7">24</text>
        <text class="value-in" x="226.5" y="151.6">26</text>
        <text class="value-in" x="244" y="147">29</text>
        <text class="value-in" x="261.5" y="147">29</text>
        <text class="value-in" x="279" y="144">31</text>
        <text class="value-in" x="296.5" y="142.5">32</text>
        <text class="value-in" x="314" y="139.5">34</text>
      </g>
      <polyline fill="none" stroke="var(--line-grey)" stroke-width=".8"
        points="121.5,138 139,134.75 156.5,125 174,112 191.5,108.75 209,102.25 226.5,95.75 244,86 261.5,86 279,79.5 296.5,73 314,73"/>
      <g fill="#fff" stroke="var(--line-grey)" stroke-width=".8">
        <circle cx="121.5" cy="138" r="1.6"/><circle cx="139" cy="134.75" r="1.6"/><circle cx="156.5" cy="125" r="1.6"/>
        <circle cx="174" cy="112" r="1.6"/><circle cx="191.5" cy="108.75" r="1.6"/><circle cx="209" cy="102.25" r="1.6"/>
        <circle cx="226.5" cy="95.75" r="1.6"/><circle cx="244" cy="86" r="1.6"/><circle cx="261.5" cy="86" r="1.6"/>
        <circle cx="279" cy="79.5" r="1.6"/><circle cx="296.5" cy="73" r="1.6"/><circle cx="314" cy="73" r="1.6"/>
      </g>
      <g>
        <text class="value-above" x="121.5" y="133">16</text>
        <text class="value-above" x="139" y="129.8">17</text>
        <text class="value-above" x="156.5" y="120">20</text>
        <text class="value-above" x="174" y="107">24</text>
        <text class="value-above" x="191.5" y="103.8">25</text>
        <text class="value-above" x="209" y="97.3">27</text>
        <text class="value-above" x="226.5" y="90.8">29</text>
        <text class="value-above" x="244" y="81">32</text>
        <text class="value-above" x="261.5" y="81">32</text>
        <text class="value-above" x="279" y="74.5">34</text>
        <text class="value-above" x="296.5" y="68">36</text>
        <text class="value-above" x="314" y="68">36</text>
      </g>
      <g class="axis-label" text-anchor="middle">
        <text x="121.5" y="198">Text</text><text x="139" y="198">Text</text><text x="156.5" y="198">Text</text>
        <text x="174" y="198">Text</text><text x="191.5" y="198">Text</text><text x="209" y="198">Text</text>
        <text x="226.5" y="198">Text</text><text x="244" y="198">Text</text><text x="261.5" y="198">Text</text>
        <text x="279" y="198">Text</text><text x="296.5" y="198">Text</text><text x="314" y="198">Text</text>
      </g>
      <text class="legend-grey" x="324" y="79">Lorem ipsum</text>
      <text class="legend-light" x="324" y="140">Lorem ipsum</text>
    </svg>
  </div>

  <!-- Slide: ranking bars with change -->
  <div class="slide slide--ranking">
    <svg viewBox="0 0 385 217">
      <text class="slide-title" x="192" y="19" text-anchor="middle">Lorem ipsum dolor sit amet</text>
      <text class="slide-lead" x="192" y="33" text-anchor="middle">Lorem ipsum dolor sit amet, consectetuer adipiscing elit. Aenean commodo ligula eget dolor.</text>
      <text class="chart-label" x="40" y="50">Lorem ipsum</text>
      <text class="micro" x="40" y="56">Lorem ipsum dolor sit amet, consectetur adipiscing elit, sed diam nonumy</text>
      <text class="micro" x="40" y="61">invidunt ut labore et dolore magna aliquyam erat, sed diam voluptua.</text>

      <g stroke="#e2e2e2" stroke-width=".5">
        <line x1="190" y1="82" x2="275" y2="82"/><line x1="190" y1="93.7" x2="275" y2="93.7"/>
        <line x1="190" y1="105.4" x2="275" y2="105.4"/><line x1="190" y1="117.1" x2="275" y2="117.1"/>
        <line x1="190" y1="128.8" x2="275" y2="128.8"/><line x1="190" y1="140.5" x2="275" y2="140.5"/>
        <line x1="190" y1="152.2" x2="275" y2="152.2"/><line x1="190" y1="163.9" x2="275" y2="163.9"/>
        <line x1="190" y1="175.6" x2="275" y2="175.6"/>
      </g>
      <g class="axis-label">
        <text x="26" y="78">Text</text><text x="26" y="89.7">Text</text><text x="26" y="101.4">Text</text>
        <text x="26" y="113.1">Text</text><text x="26" y="124.8">Text</text><text x="26" y="136.5">Text</text>
        <text x="26" y="148.2">Text</text><text x="26" y="159.9">Text</text><text x="26" y="171.6">Text</text>
        <text x="26" y="183.3">Text</text>
      </g>
      <g class="bar-dark">
        <rect x="40" y="74" width="107.9" height="4.5"/>
        <rect x="40" y="85.7" width="100.9" height="4.5"/>
        <rect x="40" y="97.4" width="100.9" height="4.5"/>
        <rect x="40" y="109.1" width="90.5" height="4.5"/>
        <rect x="40" y="120.8" width="83.5" height="4.5"/>
        <rect x="40" y="132.5" width="76.6" height="4.5"/>
        <rect x="40" y="144.2" width="73.1" height="4.5"/>
        <rect x="40" y="155.9" width="59.2" height="4.5"/>
        <rect x="40" y="167.6" width="48.7" height="4.5"/>
        <rect x="40" y="179.3" width="45.2" height="4.5"/>
      </g>
      <g class="value-end">
        <text x="150.5" y="78">31</text><text x="143.5" y="89.7">29</text><text x="143.5" y="101.4">29</text>
        <text x="133" y="113.1">26</text><text x="126" y="124.8">24</text><text x="119" y="136.5">22</text>
        <text x="115.5" y="148.2">21</text><text x="101.5" y="159.9">17</text><text x="91" y="171.6">14</text>
        <text x="87.5" y="183.3">13</text>
      </g>
      <g class="bar-light">
        <rect x="223" y="74" width="15" height="4.5"/>
        <rect x="223" y="85.7" width="20" height="4.5"/>
        <rect x="213" y="97.4" width="10" height="4.5"/>
        <rect x="218" y="109.1" width="5" height="4.5"/>
        <rect x="223" y="120.8" width="15" height="4.5"/>
        <rect x="223" y="132.5" width="15" height="4.5"/>
        <rect x="223" y="144.2" width="5" height="4.5"/>
        <rect x="218" y="155.9" width="5" height="4.5"/>
        <rect x="223" y="167.6" width="20" height="4.5"/>
        <rect x="223" y="179.3" width="10" height="4.5"/>
      </g>
      <g class="pct">
        <text x="240" y="78">+3%</text><text x="245" y="89.7">+4%</text><text x="202" y="101.4" text-anchor="end">-2%</text>
        <text x="216" y="113.1" text-anchor="end">-1%</text><text x="240" y="124.8">+3%</text><text x="240" y="136.5">+3%</text>
        <text x="230" y="148.2">+1%</text><text x="216" y="159.9" text-anchor="end">-1%</text><text x="245" y="171.6">+4%</text>
        <text x="235" y="183.3">+2%</text>
      </g>

      <use href="#bullet-block" x="286" y="75" width="90" height="36"/>
      <use href="#bullet-block" x="286" y="119" width="90" height="36"/>
      <use href="#bullet-block" x="286" y="163" width="90" height="36"/>
    </svg>
  </div>

  <div class="title-block">
    <h1 class="title-main">Standard<br>Graphs</h1>
    <p class="title-sub">SlideCraft Presentation 1</p>
  </div>
</div>
</body>
</html>
```